Rural contractor needs professional informative business card

We need a business card design that looks professional but also includes information about the services that the business offers.
The business is an earthmoving and transport business. All of the services offered are listed on the old card attached.
The business is aimed at farmers so the design we are after is a classic look. The card needs to include all of the information that is listed on the old card design uploaded as an attachment. We recognize that this is a lot of information to fit on a business card but it also operates as a key marketing tool so is very important to the business.
Feel free to send me your questions.
Thanks
Reason: We are having trouble deciding between all these great designs - thank you for your efforts
We would love to see some designs using red with a little white and black. Also feel free to re-design our logo if you feel it needs to be to fit your designs. Thank you

```html
<!DOCTYPE html>
<html lang="en">
<head>
<meta charset="utf-8">
<title>RB Hallett Contracting – Business Card</title>
<link href="https://fonts.googleapis.com/css2?family=PT+Sans:wght@400;700&display=swap" rel="stylesheet">
<style>
  :root {
    --page: #cfcfcf;
    --sky-top: #3f7fcf;
    --sky-low: #a9cdef;
    --ground: #c9b08a;
    --field: #d9bf84;
    --tan: #c8ab80;
    --gold: #e8b43c;
    --ink: #3a3124;
    --stitch: #5a4a32;
  }
  * { box-sizing: border-box; margin: 0; padding: 0; }
  html, body { width: 1200px; height: 900px; overflow: hidden; }
  body {
    background: var(--page);
    font-family: "PT Sans", sans-serif;
    color: var(--ink);
    position: relative;
  }
  .card {
    position: absolute;
    width: 560px;
    height: 320px;
    overflow: hidden;
    box-shadow: 0 6px 18px rgba(0,0,0,.25);
  }
  .card--front { left: 480px; top: 100px; }
  .card--back { left: 160px; top: 480px; }

  .photo { position: absolute; left: 0; top: 0; width: 100%; }
  .photo--trucks {
    height: 190px;
    background: linear-gradient(to bottom, var(--sky-top) 0%, var(--sky-low) 62%, var(--ground) 63%, var(--ground) 100%);
  }
  .photo--grader {
    height: 170px;
    background: linear-gradient(to bottom, var(--sky-top) 0%, var(--sky-low) 38%, var(--field) 40%, #cfae68 100%);
  }

  .band { position: absolute; left: 0; right: 0; bottom: 0; }
  .band--tan { top: 180px; background: var(--tan); }
  .band--gold { top: 160px; background: var(--gold); }

  .stitch {
    position: absolute; left: 0; right: 0; height: 0;
    border-top: 2px dashed var(--stitch);
  }

  .brand {
    position: absolute; left: 26px; top: 30px;
    display: flex; align-items: center; gap: 10px;
    font-size: 26px; font-weight: 700; color: var(--ink);
  }
  .brand__mark { width: 14px; height: 14px; background: var(--ink); }

  .contact { position: absolute; left: 32px; top: 46px; }
  .contact__name { font-size: 19px; font-weight: 700; margin-bottom: 10px; }
  .contact__line { font-size: 13px; line-height: 1.45; }
  .contact__line b { font-weight: 700; margin-right: 4px; }

  .address { position: absolute; right: 36px; top: 18px; text-align: left; }
  .address__company { font-size: 15px; font-weight: 700; margin-bottom: 6px; }
  .address__line { font-size: 13px; line-height: 1.4; }

  .tagline {
    position: absolute; right: 30px; top: 14px;
    font-size: 18px; font-weight: 700;
  }
  .services { position: absolute; top: 72px; }
  .services--earth { left: 30px; }
  .services--transport { right: 40px; }
  .services__title { font-size: 15px; font-weight: 700; margin-bottom: 3px; }
  .services__item { font-size: 12.5px; line-height: 1.4; }
</style>
</head>
<body>

  <section class="card card--front" aria-label="Business card front">
    <div class="photo photo--trucks" role="img" aria-label="Photo of prime mover trucks with flatbed trailers under a blue sky"></div>
    <div class="brand"><span class="brand__mark"></span><span>RB Hallett Contracting</span></div>
    <div class="band band--tan">
      <div class="stitch" style="top:8px"></div>
      <div class="contact">
        <p class="contact__name">Hamish Tolley</p>
        <p class="contact__line"><b>P :</b>0400 555 218</p>
        <p class="contact__line"><b>E :</b>hamish@ruralmail.example</p>
      </div>
      <div class="address">
        <p class="address__company">RB Hallett Contracting</p>
        <p class="address__line">42 Wattle Street</p>
        <p class="address__line">Dunmore 2899</p>
      </div>
    </div>
  </section>

  <section class="card card--back" aria-label="Business card back">
    <div class="photo photo--grader" role="img" aria-label="Photo of a yellow motor grader working in a harvested wheat field"></div>
    <div class="band band--gold">
      <div class="stitch" style="top:6px"></div>
      <p class="tagline">Earthmoving &amp; Transport Solutions</p>
      <div class="stitch" style="top:56px"></div>
      <div class="services services--earth">
        <p class="services__title">Earthmoving</p>
        <p class="services__item">Road Building &amp; Maintenance / Poly Pipe Laying</p>
        <p class="services__item">Clearing fence lines / Sand &amp; Gravel supplies</p>
      </div>
      <div class="services services--transport">
        <p class="services__title">Transport</p>
        <p class="services__item">Grain / Cotton</p>
        <p class="services__item">Sand &amp; Gravel / Wool</p>
      </div>
    </div>
  </section>

</body>
</html>
```